Web Design Project

Hi,
I am building a web based business within the wedding industry and I am looking for someone to design the front page of the website for me as well as the following pages/categroires which all need to be supportive of the front page
The screens will be:
Home
One Stop Reistry
Wedding Deals
Travel/Getaway
Wedding marketplace
Blog
Contact US
A more detailed view of the above is as follows:
1. Home page - be bright and capture an audience
2. Aggregate gift registries ie from key online retailers so people visiting my site can set up a bridal registry from numerous stores all in the one place ie: http://www.harwellmoss.com.au/, http://www.pellow.com.au/, http://www.qtsonix.com.au/ http://www.calvertbrame.com.au/ Something similar to http://www.vowpresentsnow.com.au
3. Aggregate the deal sites to pull all the deals relating to weddings ie: hair and make up, travel, car hire, venue hire, waxing, laser, facials, beauty treatments. Similar to http://www.everybargain.com.au/daily-deals or http://www.yesoffers.com.au/
3. We will have a tab for travel and accommodation which we want to pull the info from Travorna which I believe you can become a member and do so quite easily http://www.travorna.com.au/daily/service/affiliate-program.aspx
4. We want to build like our own tradlo/marketplace within the site where people can list things like their wedding dress, gifts they don’t want or need etc similar to http://www.secondgown.com/
5. A blog tab where we can have blogs/gossip section and build a forum for people to discuss wedding related issues similar to http://www.nuptialnest.com/wedding-forums or http://soontowed.com.au/Forums or gossip like http://www.thestarchatter.com/categories/celebrity-weddings/ The look of this section could be designed to look a bit like a gossip magazine
People need to be able to log in and out of the site and it needs to be able to be connected with pallnet and workloop as well as allowing people to subscribe to a mailing list and unsubscribe if required.
I have done a quick mock-up on powerpoint with what needs to be included but needs a lot of changing. Can be any pictures and what I have attached is not an ide ajust essentials to be on the page.
A good site to give you an idea is http://thevowline.sevenweb.com.au/

```html
<!DOCTYPE html>
<html lang="en">
<head>
<meta charset="utf-8">
<title>Bridal Shimmer — Home</title>
<link rel="stylesheet" href="https://fonts.googleapis.com/css2?family=Raleway:wght@300&family=Mulish:ital,wght@1,300&family=Arimo:wght@400;700&family=Noto+Sans:wght@700&display=swap">
<style>
  :root {
    --page-bg: #dedbd2;
    --brown-dark: #3b1d08;
    --brown-text: #5e3512;
    --brand-brown: #5a3515;
    --gold-light: #e2c06a;
    --gold-mid: #c39a45;
    --gold-dark: #a9782c;
    --signin-bg: #b5812e;
    --signin-head-top: #e7962a;
    --signin-head-bottom: #9a5d12;
    --panel-white: #ffffff;
    --body-text: #1c1c1c;
    --hero-top: #d7d2ca;
    --hero-mid: #c9bfb3;
    --hero-low: #e9e4df;
    --icon-blue: #5e9cc4;
    --icon-navy: #3d5a96;
  }
  * { box-sizing: border-box; margin: 0; padding: 0; }
  html, body { width: 1200px; height: 900px; overflow: hidden; }
  body {
    position: relative;
    background: var(--page-bg);
    font-family: "Arimo", Arial, sans-serif;
    color: var(--body-text);
  }

  /* Brand */
  .brand-mark {
    position: absolute; left: 527px; top: 18px;
    width: 120px; height: 100px; border-radius: 50%;
    background: var(--brown-dark);
  }
  .brand-name {
    position: absolute; left: 300px; top: 130px; width: 574px;
    text-align: center;
    font-family: "Raleway", sans-serif; font-weight: 300;
    font-size: 31px; letter-spacing: 5px;
    color: var(--brand-brown);
  }

  /* Navigation tabs */
  .main-nav { position: absolute; left: 0; top: 0; }
  .nav-tab {
    position: absolute; top: 174px; height: 42px;
    background: var(--brown-dark);
    border-radius: 10px 10px 0 0;
    color: #fff; font-size: 10.5px; line-height: 11px;
    display: flex; align-items: center; justify-content: center;
    text-align: center; text-decoration: none;
  }
  .nav-tab--active {
    top: 160px; height: 56px;
    background: linear-gradient(180deg, var(--gold-light), var(--gold-mid) 55%, var(--gold-dark));
    color: #2a1606;
  }

  /* Content panel */
  .content-panel {
    position: absolute; left: 166px; top: 216px; width: 890px; height: 670px;
    background: var(--panel-white);
    border-radius: 10px 10px 16px 16px;
    box-shadow: 0 3px 8px rgba(0,0,0,0.25);
    overflow: hidden;
  }
  .hero {
    position: absolute; left: 0; top: 0; width: 890px; height: 321px;
    background:
      radial-gradient(ellipse 260px 300px at 360px 240px, #efe7df 0%, rgba(239,231,223,0) 70%),
      linear-gradient(180deg, var(--hero-top) 0%, var(--hero-mid) 45%, var(--hero-low) 100%);
  }
  .hero-tagline {
    position: absolute; left: 393px; top: 22px;
    font-family: "Mulish", sans-serif; font-style: italic; font-weight: 300;
    font-size: 21.5px; line-height: 25px; color: #4a3a2e;
  }
  .hero-arrow {
    position: absolute; top: 138px; width: 26px; height: 54px;
    background: #fff;
  }
  .hero-arrow--prev { left: 0; border-radius: 0 27px 27px 0; }
  .hero-arrow--next { right: 0; border-radius: 27px 0 0 27px; }
  .hero-arrow svg { position: absolute; top: 19px; }
  .hero-arrow--prev svg { left: 4px; }
  .hero-arrow--next svg { left: 10px; }

  .article { position: absolute; left: 36px; top: 345px; width: 510px; }
  .article h1 {
    font-family: "Noto Sans", Verdana, sans-serif; font-weight: 700;
    font-size: 21px; color: var(--brown-text); margin-bottom: 12px;
  }
  .article h2 {
    font-family: "Noto Sans", Verdana, sans-serif; font-weight: 700;
    font-size: 16.5px; color: var(--brown-text); margin: 14px 0 16px;
  }
  .article p { font-size: 10.4px; line-height: 13.6px; }

  .site-footer {
    position: absolute; left: 0; bottom: 0; width: 890px; height: 28px;
    background: var(--brown-dark);
    display: flex; align-items: center; justify-content: center;
    color: #fff; font-size: 11px;
  }
  .site-footer a { color: #fff; text-decoration: none; }
  .site-footer .sep { margin: 0 5px; }

  /* Sign in */
  .signin {
    position: absolute; left: 771px; top: 439px; width: 235px; height: 268px;
    background: var(--signin-bg);
    border-radius: 12px;
    box-shadow: 0 2px 6px rgba(0,0,0,0.3);
    overflow: hidden;
  }
  .signin-head {
    height: 46px; padding: 13px 0 0 23px;
    background: linear-gradient(180deg, var(--signin-head-top), var(--signin-head-bottom));
    color: #fff; font-size: 13px; letter-spacing: 0.5px;
  }
  .signin label { position: absolute; left: 25px; font-size: 11px; color: #111; }
  .signin-field {
    position: absolute; left: 24px; width: 190px; height: 28px;
    background: #fff; border: 0;
  }
  .signin-link { position: absolute; left: 24px; font-size: 13px; color: #1a1006; text-decoration: none; }
  .subscribe { position: absolute; left: 22px; top: 218px; display: flex; align-items: center; }
  .subscribe-text { margin-left: 13px; width: 120px; font-size: 11px; line-height: 14px; color: #1a1006; }

  .social-links { position: absolute; left: 795px; top: 729px; }
  .social-link {
    display: flex; align-items: center; margin-bottom: 11px;
    font-size: 11px; color: #222; text-decoration: none;
  }
  .social-square { width: 37px; height: 38px; border-radius: 4px; margin-right: 10px; }
  .social-square--chirpa { background: var(--icon-blue); }
  .social-square--pallnet { background: var(--icon-navy); }
</style>
</head>
<body>

<header>
  <div class="brand-mark" aria-hidden="true"></div>
  <div class="brand-name">BRIDAL SHIMMER</div>
  <nav class="main-nav">
    <a class="nav-tab nav-tab--active" href="#" style="left:237px;width:108px;">Home</a>
    <a class="nav-tab" href="#" style="left:345px;width:106px;">One Stop<br>Registry</a>
    <a class="nav-tab" href="#" style="left:451px;width:107px;">Wedding Deals</a>
    <a class="nav-tab" href="#" style="left:558px;width:107px;">Travel /<br>Accommodation<br>Gateway</a>
    <a class="nav-tab" href="#" style="left:665px;width:108px;">Wedding<br>Marketplace<br>(pre-owned treasures)</a>
    <a class="nav-tab" href="#" style="left:773px;width:107px;">Gossip/Editorial</a>
    <a class="nav-tab" href="#" style="left:880px;width:108px;">Booking Engine</a>
  </nav>
</header>

<main class="content-panel">
  <section class="hero" role="img" aria-label="Photograph of a bride in a strapless lace gown reclining among pale pink and white flowers">
    <p class="hero-tagline">Soulmates...two halves of the<br>same soul joining together in lifes journey</p>
    <span class="hero-arrow hero-arrow--prev"><svg width="12" height="16" viewBox="0 0 12 16"><path d="M10 0 L0 8 L10 16 Z" fill="#2a1a0e"/></svg></span>
    <span class="hero-arrow hero-arrow--next"><svg width="12" height="16" viewBox="0 0 12 16"><path d="M0 0 L10 8 L0 16 Z" fill="#2a1a0e"/></svg></span>
  </section>

  <article class="article">
    <h1>Header 1</h1>
    <p>Untios eum as doloremporro conem. Sapel ipid quam, ommoluptate eos illecto rersperernam quatinit etur simin ratquas dolorum quos eum faccus quiati ut quiduntur rehenem que volent expliti untinihil ipsame re, se ius sam veruptatus eaqui cum que nobitiberist odis doluptam eium volupiendus et expernatur sequi nonsequ odipsunt et pa volorpo rercil ma nos nim es evendio blab ium estion et, aut ex es di aut escimus asit quo officia quo iusandit imillup tatust od et verferi andeles tiorrum et, sit eatecus temporibus as il minvendi odis rernata spicta doluptam as eost atur restiae pa sant et que volupietur re placcumet qui odi veliatecto officimus pereri anditem fugiania dolorit hillabore poriorrovid quam, officia ndipsa ium at. Busdam ut quaspideni dis siti oditae poreped quiae nulpa simusae simus re et assequi con parciatur?</p>
    <h2>Header 2</h2>
    <p>Untios eum as doloremporro conem. Sapel ipid quam, ommoluptate eos illecto rersperernam quatinit etur simin ratquas dolorum quos eum faccus quiati ut quiduntur rehenem que volent expliti untinihil ipsame re, se ius sam veruptatus eaqui cum que nobitiberist odis doluptam eium volupiendus et expernatur sequi nonsequ odipsunt et pa volorpo rercil ma nos nim es evendio blab ium estion et, aut ex es di aut escimus asit quo officia quo iusanolorit hillabore poriorrovid quam, officia ndipsa ium at.<br>Busdam ut quaspideni dis siti oditae poreped quiae nulpa simusae simus re et assequi con parciatur?</p>
  </article>

  <footer class="site-footer">
    <a href="#">About</a><span class="sep">|</span>
    <a href="#">Advertise with us</a><span class="sep">|</span>
    <a href="#">Contact us</a><span class="sep">|</span>
    <a href="#">Terms &amp; Conditions</a><span class="sep">|</span>
    <a href="#">Privacy Policy</a>
  </footer>
</main>

<aside class="signin">
  <div class="signin-head">SIGN IN</div>
  <label for="username" style="top:65px;">User name</label>
  <input class="signin-field" id="username" type="text" style="top:82px;">
  <label for="password" style="top:119px;">Passowrd</label>
  <input class="signin-field" id="password" type="password" style="top:137px;">
  <a class="signin-link" href="#" style="top:174px;">ForgottenPassword</a>
  <a class="signin-link" href="#" style="top:195px;">Join Now</a>
  <div class="subscribe">
    <svg width="36" height="36" viewBox="0 0 36 36" aria-hidden="true">
      <rect x="0.5" y="0.5" width="35" height="35" rx="5" fill="#eef1f4" stroke="#c9d0d6"/>
      <rect x="5" y="10" width="26" height="17" fill="#f7f8fa" stroke="#9aa5ae"/>
      <path d="M5 10 L18 20 L31 10" fill="none" stroke="#9aa5ae" stroke-width="1.2"/>
    </svg>
    <span class="subscribe-text">Subscribe to ur mail-ing list</span>
  </div>
</aside>

<div class="social-links">
  <a class="social-link" href="#"><span class="social-square social-square--chirpa"></span>Follow us on Chirpa</a>
  <a class="social-link" href="#"><span class="social-square social-square--pallnet"></span>Join our Pallnet group</a>
</div>

</body>
</html>
```